Refresh American History Book Cover

We would like a new book cover based on the attached old book cover. Please maintain a very strong resemblance to the cover, but we would be open to a bit of a freshening up of the design. We would like to use the same illustrations since they match the illustrations inside. Please fix the whale! It's head should not be cut off!

We are using this for Vextora Quillmark Self Printing in a 6" x 9" format.

```html
<!DOCTYPE html>
<html lang="en">
<head>
<meta charset="utf-8">
<title>Hexes, Tides, Crinolines &amp; Canvas — Book Cover</title>
<link href="https://fonts.googleapis.com/css2?family=Marcellus&family=Libre+Baskerville&family=Great+Vibes&display=swap" rel="stylesheet">
<style>
  :root {
    --backdrop: #c55a41;
    --navy: #1f2f5d;
    --ivory: #ecebe8;
    --coral: #d8603f;
    --band: #ecebea;
  }
  html, body {
    margin: 0;
    padding: 0;
    width: 1200px;
    height: 800px;
    overflow: hidden;
    background: var(--backdrop);
  }
  .cover {
    position: absolute;
    left: 400px;
    top: 94px;
    width: 400px;
    height: 610px;
    background: var(--navy);
    border-radius: 3px;
    overflow: hidden;
  }
  .title {
    margin: 0;
    font-weight: 400;
  }
  .title-line {
    position: absolute;
    left: 0;
    width: 100%;
    text-align: center;
    font-family: "Marcellus", serif;
    font-weight: 400;
    color: var(--ivory);
    font-size: 56px;
    line-height: 1;
    letter-spacing: -1px;
    transform: scaleY(1.15);
    transform-origin: top center;
    white-space: nowrap;
  }
  .title-hexes { top: 30px; }
  .title-tides { top: 102px; }
  .title-crinolines { top: 175px; font-size: 50px; }
  .title-amp { top: 250px; font-size: 52px; }
  .title-canvas { top: 318px; }
  .whale {
    position: absolute;
    top: 104px;
    width: 108px;
    height: 60px;
  }
  .whale-left { left: 0; }
  .whale-right { right: 0; }
  .ship {
    position: absolute;
    left: 97px;
    top: 378px;
    width: 180px;
    height: 126px;
  }
  .subtitle-band {
    position: absolute;
    left: 0;
    top: 507px;
    width: 100%;
    height: 45px;
    background: var(--band);
    display: flex;
    align-items: center;
    justify-content: center;
  }
  .subtitle {
    margin: 0;
    font-family: "Libre Baskerville", serif;
    font-size: 12.4px;
    line-height: 1.35;
    text-align: center;
    color: var(--navy);
  }
  .author {
    position: absolute;
    left: 0;
    width: 100%;
    top: 560px;
    margin: 0;
    text-align: center;
    font-family: "Great Vibes", cursive;
    font-size: 31px;
    color: var(--coral);
    line-height: 1.1;
  }
</style>
</head>
<body>
  <main class="cover">
    <svg class="whale whale-left" viewBox="0 0 108 60" role="img" aria-label="Illustration of a spouting whale in waves">
      <defs>
        <linearGradient id="whaleFill" x1="0" y1="0" x2="0" y2="1">
          <stop offset="0" stop-color="#1f2f5d" stop-opacity="0"/>
          <stop offset="0.35" stop-color="#c85a3e" stop-opacity="0.55"/>
          <stop offset="1" stop-color="#d8603f" stop-opacity="0.8"/>
        </linearGradient>
      </defs>
      <rect x="0" y="0" width="108" height="60" rx="6" fill="url(#whaleFill)"/>
    </svg>
    <svg class="whale whale-right" viewBox="0 0 108 60" role="img" aria-label="Illustration of a spouting whale in waves">
      <rect x="0" y="0" width="108" height="60" rx="6" fill="url(#whaleFill)"/>
    </svg>

    <h1 class="title">
      <span class="title-line title-hexes">HEXES</span>
      <span class="title-line title-tides">TIDES</span>
      <span class="title-line title-crinolines">CRINOLINES</span>
      <span class="title-line title-amp">&amp;</span>
      <span class="title-line title-canvas">CANVAS</span>
    </h1>

    <svg class="ship" viewBox="0 0 180 126" role="img" aria-label="Line illustration of a full-rigged sailing ship on waves">
      <defs>
        <radialGradient id="shipFill" cx="0.5" cy="0.55" r="0.6">
          <stop offset="0" stop-color="#d8603f" stop-opacity="0.75"/>
          <stop offset="1" stop-color="#d8603f" stop-opacity="0.15"/>
        </radialGradient>
      </defs>
      <rect x="0" y="0" width="180" height="126" rx="8" fill="url(#shipFill)"/>
    </svg>

    <div class="subtitle-band">
      <p class="subtitle">EXPLOITS AND MISHAPS FROM<br>THREE CENTURIES OF HARBOR TOWN HISTORY</p>
    </div>

    <p class="author">Delia Harrowgate</p>
  </main>
</body>
</html>
```